Vitamin B12 Liquid Drops Label

hi, i need a label designed for my vitamin b12 drops that i am going to be selling on bazaroo. the label needs to quickly capture the attention of a buyer as he or she is scrolling through the thumbnail search results on bazaroo.example my brand is called zulpa. i already have an example brand logo i will be using, however, i need help designing the rest of the label. attached are some examples of labels i like for other supplements.some of these examples are pink. i do not want pink. please go for a blue/green color scheme. THE DESIGN MUST BE BOLD

Target Market(s)

adults ages 30 - 64

Font styles to use
Sans Serif

Colors
0455a3
cedeed
3176b5
85acd3
cfdeed
9bcb3b
abd037
cadf82
00a990

Requirements
Must have
• - bold design
• - somewhat gender-neutral color scheme because this will be used equally by men and women
• - B12 MUST be very prominent and visible on the label
Should not have
• - it should not be "crunchy" looking

```html
<!DOCTYPE html>
<html lang="en">
<head>
<meta charset="utf-8">
<title>Zulpa Vitamin B12 Drops Label</title>
<link rel="stylesheet" href="https://fonts.googleapis.com/css2?family=Montserrat:wght@800;900&display=swap">
<style>
  :root {
    --navy: #0455a3;
    --mid-blue: #3176b5;
    --sky: #85acd3;
    --ice: #cedeed;
    --lime: #9bcb3b;
    --lime-edge: #abd037;
    --lime-pale: #cadf82;
    --white: #ffffff;
    --ink: #000000;
  }
  html, body {
    margin: 0;
    padding: 0;
    width: 1200px;
    height: 491px;
    overflow: hidden;
    background: var(--white);
  }
  .label {
    display: block;
    width: 1200px;
    height: 491px;
  }
  .label text {
    font-family: "Montserrat", Arial, sans-serif;
  }
  .big-b12 { fill: var(--mid-blue); font-weight: 900; }
  .brand-name { fill: var(--ice); font-weight: 900; }
  .product-name { fill: var(--ice); font-weight: 800; }
  .facts-title { fill: var(--ink); font-weight: 800; }
</style>
</head>
<body>
<svg class="label" viewBox="0 0 1500 614" xmlns="http://www.w3.org/2000/svg" role="group" aria-label="Zulpa Vitamin B12 Drops label">
  <defs>
    <linearGradient id="stripe-fill" x1="0" y1="0" x2="1" y2="0">
      <stop offset="0" stop-color="#3176b5"/>
      <stop offset="0.5" stop-color="#5189c0"/>
      <stop offset="1" stop-color="#3176b5"/>
    </linearGradient>
  </defs>

  <!-- lower chevron-stripe field -->
  <rect class="stripe-field" x="300" y="190" width="1200" height="424" fill="url(#stripe-fill)" role="img" aria-label="Diagonal chevron stripes in mid blue and sky blue"/>

  <!-- light divider band -->
  <rect class="divider-band" x="300" y="190" width="1200" height="28" fill="var(--ice)"/>

  <!-- top title band -->
  <rect class="title-band" x="300" y="0" width="1200" height="190" fill="var(--navy)"/>

  <!-- left green chevron -->
  <polygon class="chevron-pale" points="305,0 357,0 542,300 357,614 305,614 490,300" fill="var(--lime-pale)"/>
  <polygon class="chevron-edge" points="305,0 330,0 515,300 330,614 305,614 490,300" fill="var(--lime-edge)"/>
  <polygon class="chevron-main" points="0,0 305,0 490,300 305,614 0,614" fill="var(--lime)"/>

  <!-- vertical B12 -->
  <text class="big-b12" x="0" y="0" font-size="335" letter-spacing="-10" text-anchor="middle" dominant-baseline="central" transform="translate(150 305) rotate(-90)">B12</text>

  <!-- brand name -->
  <text class="brand-name" x="470" y="155" font-size="158" letter-spacing="-2">ZULPA</text>

  <!-- divider slash -->
  <line class="slash" x1="1035" y1="162" x2="1112" y2="26" stroke="var(--sky)" stroke-width="24"/>

  <!-- product name -->
  <text class="product-name" x="1122" y="81" font-size="56">VITAMIN</text>
  <text class="product-name" x="1122" y="151" font-size="56">B12 DROPS</text>

  <!-- nutrition facts panel -->
  <rect class="facts-panel" x="1245" y="240" width="236" height="356" fill="var(--white)"/>
  <text class="facts-title" x="1257" y="268" font-size="21">Nutrition Facts</text>
</svg>
</body>
</html>
```